New Facebook Banner

Hi
We are operating Ramen shop in Australia.(http://mizunokobowls.com)
I want to create new design for our Facebook banner and title is "Free Ramen on your Birthday".
Sample attached is our existing banner design. We would like to make it more modern and sophisticated.
We are so looking forward to seeing your design for our free ramen promotion.

https://www.facebook.com/mizunokobowls/

Industry/Entity Type

Japanese Restaurant

Font styles to use
Sans Serif

```html
<!DOCTYPE html>
<html lang="en">
<head>
<meta charset="utf-8">
<title>Free Ramen on your Birthday – Mizunoko Bowls</title>
<link href="https://fonts.googleapis.com/css2?family=Fredoka:wght@500&family=Kaushan+Script&family=Lilita+One&family=Montserrat:wght@600&display=swap" rel="stylesheet">
<style>
  :root {
    --bg-light: #fbfbfb;
    --bg-soft: #ececec;
    --plum: #6a3a78;
    --ribbon: #5c2f6a;
    --pink: #e2317d;
    --green: #8fd65a;
    --balloon-red: #e8373a;
    --balloon-purple: #a346c9;
    --balloon-orange: #f39a2a;
    --balloon-green: #7fcf4e;
    --balloon-yellow: #f2d33a;
    --bowl-dark: #2e3b4a;
    --broth: #e9b38f;
  }
  * { margin: 0; padding: 0; box-sizing: border-box; }
  html, body { width: 1200px; height: 444px; overflow: hidden; }
  .banner {
    position: relative;
    width: 1200px;
    height: 444px;
    overflow: hidden;
    background: radial-gradient(ellipse at 50% 50%, var(--bg-light) 40%, var(--bg-soft) 100%);
  }

  /* Illustration areas: flat gradient placeholders */
  .party-decor { position: absolute; opacity: .55; }
  .party-decor--left {
    left: 0; top: 0; width: 300px; height: 330px;
    border-bottom-right-radius: 60px;
    background: linear-gradient(160deg, var(--balloon-orange) 0%, var(--balloon-red) 40%, var(--balloon-purple) 70%, var(--balloon-green) 100%);
  }
  .party-decor--top {
    left: 300px; top: 0; width: 170px; height: 110px;
    border-bottom-right-radius: 40px;
    background: linear-gradient(120deg, var(--balloon-purple) 0%, var(--balloon-green) 100%);
  }
  .party-decor--right {
    left: 870px; top: 0; width: 330px; height: 290px;
    border-bottom-left-radius: 60px;
    background: linear-gradient(200deg, var(--balloon-green) 0%, var(--balloon-purple) 35%, var(--balloon-orange) 65%, var(--balloon-yellow) 100%);
  }
  .ramen-bowl {
    position: absolute;
    top: 233px;
    width: 220px;
    height: 177px;
    border-radius: 24px;
    background: linear-gradient(180deg, var(--broth) 0%, var(--broth) 35%, var(--bowl-dark) 70%);
  }
  .ramen-bowl--left { left: 110px; }
  .ramen-bowl--right { left: 855px; }

  /* Headline */
  .headline { position: absolute; inset: 0; text-align: center; }
  .headline__free {
    position: absolute; left: 0; right: 0; top: 90px;
    font-family: "Fredoka", sans-serif; font-weight: 500;
    font-size: 78px; line-height: 1; letter-spacing: 2px;
    color: var(--plum);
  }
  .headline__ramen {
    position: absolute; left: 0; right: 0; top: 160px;
    font-family: "Kaushan Script", cursive;
    font-size: 100px; line-height: 1;
    color: var(--pink);
  }
  .headline__ribbon {
    position: absolute; left: 491px; top: 263px;
    width: 218px; height: 38px;
  }
  .headline__ribbon-text {
    position: absolute; left: 491px; top: 263px;
    width: 218px; height: 38px;
    font-family: "Fredoka", sans-serif; font-weight: 500;
    font-size: 22px; line-height: 38px;
    color: #fff; text-align: center;
  }
  .headline__birthday {
    position: absolute; left: 0; right: 0; top: 322px;
    font-family: "Lilita One", sans-serif;
    font-size: 84px; line-height: 1; letter-spacing: 3px;
    color: var(--green);
    transform: skewX(-8deg);
  }
  .website {
    position: absolute; left: 0; right: 0; top: 410px;
    text-align: center;
    font-family: "Montserrat", sans-serif; font-weight: 600;
    font-size: 21px; line-height: 1; letter-spacing: 9px;
    color: var(--plum);
  }
</style>
</head>
<body>
<main class="banner">
  <div class="party-decor party-decor--left" role="img" aria-label="Illustration of colourful party balloons and bunting flags"></div>
  <div class="party-decor party-decor--top" role="img" aria-label="Illustration of purple and green balloons with bunting"></div>
  <div class="party-decor party-decor--right" role="img" aria-label="Illustration of orange, purple and yellow party balloons with bunting"></div>

  <div class="ramen-bowl ramen-bowl--left" role="img" aria-label="Illustration of a steaming bowl of ramen with egg, nori and chopsticks"></div>
  <div class="ramen-bowl ramen-bowl--right" role="img" aria-label="Illustration of a steaming bowl of ramen with egg, nori and chopsticks"></div>

  <section class="headline">
    <h1 class="headline__free">FREE</h1>
    <p class="headline__ramen">Ramen</p>
    <svg class="headline__ribbon" viewBox="0 0 218 38" aria-hidden="true">
      <polygon points="0,0 218,0 204,19 218,38 0,38 14,19" fill="var(--ribbon)"/>
    </svg>
    <p class="headline__ribbon-text">on your</p>
    <p class="headline__birthday">BIRTHDAY</p>
  </section>

  <p class="website">www.mizunokobowls.com</p>
</main>
</body>
</html>
```